Yoga By Marisol Ad for print

I need a print ad designed to go in a brochure for a charity event. I've attached the specs. I need the specs for the 1/2 page ad.
Text for ad:

“E-RYT 200 extensive training with Asana Scholars
Social Media Influencer
Offering group, private and corporate yoga classes
Email: info@yogabymarisol-studio.com
Web: www.yogabymarisol-studio.com
Phone: 480-555-0163
Instagram: @flowofmarisol

Target Market(s)

Yoga practitioners and businesses looking to bring yoga in to their operation.

Font styles to use
Serif
Script

Colors
eda3c7
e34197
eea4c8
f9d9e8
feeeee
000000
1b1b1b
cbcbcb
eaeaea

Requirements
Must have
• One version of my logo, I have provided many to choose from for best aesthetic appeal

```html
<!DOCTYPE html>
<html lang="en">
<head>
<meta charset="utf-8">
<title>Yoga By Marisol – Print Ad</title>
<link rel="stylesheet" href="https://fonts.googleapis.com/css2?family=Cinzel:wght@400;500&family=Tinos:wght@400;700&display=swap">
<style>
  :root {
    --page-bg: #eef0f3;
    --poster-top: #f4f5f7;
    --poster-bottom: #e2e4e8;
    --band-blue: #2a8fc1;
    --accent-pink: #e0607a;
    --white: #ffffff;
    --skin: #e6b89c;
    --top-pink: #f1a3a0;
    --pants-blue: #2f8fc4;
  }
  * { margin: 0; padding: 0; box-sizing: border-box; }
  html, body { width: 1200px; height: 1200px; overflow: hidden; background: var(--page-bg); }
  .ad {
    position: absolute; left: 188px; top: 0;
    width: 824px; height: 1200px; overflow: hidden;
    background: linear-gradient(160deg, var(--poster-top), var(--poster-bottom));
  }
  .photo-portrait {
    position: absolute; left: 13px; top: 158px; width: 274px; height: 418px;
    background: linear-gradient(180deg, #eccfb6 0%, #d9a98f 40%, #b9a3a0 100%);
    border-radius: 40% 40% 12% 12%;
  }
  .photo-stretch { position: absolute; inset: 0; z-index: 3; }
  .brand-name {
    position: absolute; left: 290px; top: 472px; width: 270px;
    text-align: center; font-family: "Cinzel", serif; font-weight: 500;
    font-size: 40px; color: var(--accent-pink);
  }
  .credential-band {
    position: absolute; left: 0; top: 575px; width: 545px; height: 169px;
    background: var(--band-blue); padding: 18px 0 0 30px;
    font-family: "Cinzel", serif; font-size: 36px; line-height: 47px; color: var(--white);
  }
  .highlights {
    position: absolute; left: 30px; top: 772px; width: 560px;
    font-family: "Cinzel", serif; font-size: 33px; line-height: 42px; color: var(--accent-pink);
  }
  .highlights p + p { margin-top: 30px; }
  .contact-band {
    position: absolute; left: 0; top: 985px; width: 824px; height: 215px;
    background: var(--band-blue); padding: 28px 0 0 30px;
    font-family: "Tinos", serif; color: var(--white);
  }
  .contact-band .line { font-size: 27px; line-height: 33px; }
  .contact-band .line.strong { font-weight: 700; font-size: 30px; line-height: 40px; }
  .contact-band .line.gap { margin-top: 8px; }
</style>
</head>
<body>
  <main class="ad">
    <div class="photo-portrait" role="img" aria-label="Photo of the instructor crouching in a yoga pose with palms together"></div>

    <div class="brand-name">Marisol Flow</div>

    <div class="credential-band">E-RYT 200 extensive<br>training with Asana<br>Scholars</div>

    <div class="highlights">
      <p>Social Media Influencer</p>
      <p>Offering group, private &amp;<br>corporate yoga classes</p>
    </div>

    <div class="contact-band">
      <div class="line">info@yogabymarisol-studio.com</div>
      <div class="line">www.yogabymarisol-studio.com</div>
      <div class="line strong gap">Phone: 480-555-0163</div>
      <div class="line strong">Instagram: @flowofmarisol</div>
    </div>

    <svg class="photo-stretch" viewBox="0 0 824 1200" width="824" height="1200" role="img" aria-label="Photo of the instructor seated cross-legged, stretching one arm overhead">
      <defs>
        <linearGradient id="stretch-tones" x1="0" y1="0" x2="0" y2="1">
          <stop offset="0" stop-color="var(--skin)"/>
          <stop offset="0.5" stop-color="var(--top-pink)"/>
          <stop offset="0.72" stop-color="var(--skin)"/>
          <stop offset="0.8" stop-color="var(--pants-blue)"/>
          <stop offset="1" stop-color="var(--pants-blue)"/>
        </linearGradient>
      </defs>
      <path d="M640 0 H824 V1200 H420 Q375 1100 420 1010 Q520 955 640 960 Z" fill="url(#stretch-tones)"/>
    </svg>
  </main>
</body>
</html>
```